I want a business letter head designed, one that I can have printed but also one that I can use as an insert for proforma documentation that is printed in house.

Business name : RJ Penfold & Associates
Address: PO Box 738
Tewantin Qld 4587

Type of business: Accounting practice- accounting, taxation, audit, self managed superannuation,

Colour scheme: black and blue - previously designed a business card; however the blue that is one the cards is very washed out and I am not particularly happy with it.

Industry/Entity Type

Business

```html
<!DOCTYPE html>
<html lang="en">
<head>
<meta charset="utf-8">
<title>RJ Penfold &amp; Associates — Letterhead</title>
<link href="https://fonts.googleapis.com/css2?family=Crimson+Pro:wght@400;700&display=swap" rel="stylesheet">
<style>
  :root {
    --ink: #111111;
    --band: #2e2e2e;
    --cyan: #00f0ff;
    --paper: #ffffff;
    --paper-shade: #ececec;
    --stage: #d9d9d9;
    --rule: #555555;
  }
  html, body {
    margin: 0;
    width: 923px;
    height: 1200px;
    overflow: hidden;
    background: var(--stage);
  }
  .letterhead {
    position: absolute;
    left: 24px;
    top: 44px;
    width: 863px;
    height: 1116px;
    background: linear-gradient(90deg, var(--paper-shade) 0%, var(--paper) 45%);
    font-family: "Crimson Pro", "Times New Roman", serif;
    color: var(--ink);
    overflow: hidden;
  }
  .brand {
    position: absolute;
    left: 14px;
    top: 31px;
    display: flex;
    align-items: center;
    gap: 24px;
  }
  .brand-square {
    width: 84px;
    height: 80px;
    background: var(--cyan);
  }
  .brand-name {
    margin: 0;
    font-weight: 700;
    font-size: 36px;
    line-height: 34px;
  }
  .brand-name span { display: block; }
  .brand-name .first { padding-left: 18px; }
  .contact {
    position: absolute;
    left: 610px;
    top: 20px;
    padding-left: 10px;
    border-left: 1px solid var(--rule);
    font-size: 15px;
    line-height: 20px;
  }
  .contact-line {
    display: flex;
    align-items: center;
    gap: 6px;
  }
  .contact-line svg { fill: var(--ink); }
  .services {
    list-style: none;
    margin: 6px 0 0;
    padding: 0;
    line-height: 18px;
  }
  .services li::before {
    content: "• ";
  }
  .services .inline { margin-left: 12px; }
  .footer-waves {
    position: absolute;
    left: 0;
    bottom: 0;
  }
  .address {
    position: absolute;
    left: 540px;
    top: 1028px;
    width: 220px;
    text-align: center;
    color: var(--paper);
    font-size: 18px;
    line-height: 22px;
  }
</style>
</head>
<body>
  <main class="letterhead">
    <header class="brand">
      <div class="brand-square" aria-hidden="true"></div>
      <h1 class="brand-name"><span class="first">RJ Penfold</span><span>&amp; Associates.</span></h1>
    </header>

    <section class="contact">
      <div class="contact-line">
        <svg width="8" height="12" viewBox="0 0 8 12" aria-hidden="true"><rect x="0" y="0" width="8" height="12" rx="1.5"/><rect x="1.5" y="1.5" width="5" height="4" fill="#fff"/></svg>
        0438216907
      </div>
      <div class="contact-line">
        <svg width="11" height="8" viewBox="0 0 11 8" aria-hidden="true"><rect width="11" height="8"/><path d="M0 0 L5.5 4.5 L11 0" stroke="#fff" stroke-width="1" fill="none"/></svg>
        jess@rjpenfoldassociates.com.au
      </div>
      <ul class="services">
        <li>Accounting Practice- Accounting</li>
        <li>Taxation <span class="inline">• Audit</span></li>
        <li>Self Managed Superannuation</li>
      </ul>
    </section>

    <svg class="footer-waves" width="863" height="260" viewBox="24 900 863 260" aria-hidden="true">
      <path d="M24,1000 C40,1062 120,1104 260,1106 C420,1108 560,1074 680,1074 C770,1075 840,1112 887,1160 L24,1160 Z" fill="var(--cyan)"/>
      <path d="M30,1005 C52,1060 130,1090 260,1092 C420,1094 560,1060 680,1061 C780,1062 850,1108 887,1148" fill="none" stroke="var(--band)" stroke-width="8"/>
      <path d="M24,915 C30,1012 120,1076 260,1083 C340,1087 400,1080 440,1073 C380,1078 320,1080 260,1077 C130,1068 48,1012 24,968 Z" fill="var(--cyan)"/>
    </svg>

    <address class="address" style="font-style:normal">PO Box 738<br>Tewantin Qld 4587</address>
  </main>
</body>
</html>
```